Web app for social movements needs a new look

We are building a Corvex Glide extension called "Rise Up" that helps social movement leaders and advocacy organizations connect with an audience that cares about their cause, and we need to create a more polished website to explain the extension to prospective users. The extension analyzes articles users are reading online and recommends ways they can take action in their local area on the social and political issues they are reading about. For example, if a user is reading about the climate crisis, the extension might display a banner recommending a rally being held by the Tidewater Coalition or an opportunity to canvass or phone bank for a pro-Blue Harbor Pact political candidate. Organizers with progressive organizations can register for an account on our web portal to start posting actions or events that will then be recommended to users through the browser extension if they are reading a relevant article.

We are planning for an upcoming "soft launch" and would like to create a more polished version of our website. The design should include:
– A user-facing page that that concisely explains how the Glide extension works and links to the Glide web store where users can download Rise Up.
– An organizer-facing page that outlines the steps involved for organizers to recommend their organization or a specific action to users through Rise Up: register for an account, post an action or event, your action or event is recommended to users.
– An HTML/CSS template for the organizer portal that we can then take and populate with Pellucid forms or other Pellucid content. This template should include a top menu bar. We've provided an example of the extremely barebones template used in our prototype as an example (base.html).
– A redesigned or improved logo, including one version designed to be put on a white background and one version designed to go on a background of a darker color (e.g., orange). Our current logo is provided. Feel free to use this as a starting point or design something completely different.

The design should convey themes of solidarity, bringing people together to effect positive change, and hope for a better future. We expect that organizations and users on the platform will be focused on a range of progressive issues, including racial justice, immigration justice, gender equity, LGBTQ+ rights, workers' rights, and addressing the climate crisis and economic inequality.

Currently, the color scheme of our prototype browser extension is centered around the color orange, but we are open to designers' ideas about other possible color schemes.

```html
<!DOCTYPE html>
<html lang="en">
<head>
<meta charset="utf-8">
<title>Rise Up</title>
<link rel="stylesheet" href="https://fonts.googleapis.com/css2?family=Montserrat:wght@600;700;800&family=Lato:wght@300;400&display=swap">
<style>
:root{
  --orange:#e8683a;
  --orange-mid:#f08060;
  --orange-soft:#f0aa98;
  --peach:#ffc08a;
  --ink:#1d1d1d;
  --text:#333;
  --grey-bg:#f5f4f4;
  --footer:#232323;
  --rule:#555;
}
*{margin:0;padding:0;box-sizing:border-box}
html,body{width:732px;height:1200px;overflow:hidden;background:#fff}
body{position:relative;font-family:"Lato",sans-serif;color:var(--text)}
.abs{position:absolute}
.heading{font-family:"Montserrat",sans-serif;font-weight:800;color:var(--ink);letter-spacing:.2px}

.hero{position:absolute;left:0;top:0;width:732px;height:279px;background:radial-gradient(ellipse at 50% 40%,#4a3a34 0%,#2c2522 55%,#1b1716 100%)}
.brand{display:flex;align-items:center;gap:6px}
.brand-dot{width:41px;height:41px;border-radius:50%;background:var(--peach)}
.brand-name{font-family:"Lato",sans-serif;font-size:13px;color:var(--orange);font-weight:400}
.nav{top:20px;right:80px;display:flex;align-items:center;gap:0}
.nav a{color:#fff;font-size:8.5px;text-decoration:none;margin-left:18px}
.nav .login{background:var(--orange);padding:5px 8px;font-weight:400}
.hero-title{top:95px;width:732px;text-align:center;font-family:"Montserrat",sans-serif;font-weight:800;font-size:17px;color:#fff}
.hero-lead{top:130px;width:732px;text-align:center;font-size:10px;line-height:16px;color:#fff}
.cta{top:178px;left:304px;width:126px;height:28px;background:var(--orange);color:#fff;font-family:"Montserrat",sans-serif;font-weight:700;font-size:10px;display:flex;align-items:center;justify-content:center;text-decoration:none}

.section-title{width:732px;text-align:center;font-size:11.5px}
.rule{height:1.5px;background:var(--rule)}
.step{width:130px;text-align:center}
.step h3{font-family:"Montserrat",sans-serif;font-weight:700;font-size:7.5px;color:var(--ink);margin-bottom:8px}
.step p{font-size:6.6px;line-height:8.8px;color:#333}

.overview{top:602px;left:0;width:732px;height:242px;background:var(--grey-bg)}
.overview-body{left:370px;top:668px;width:280px;font-size:8.5px;line-height:13.7px;color:#333;text-align:justify}
.overview-body p+p{margin-top:14px}

.person{width:110px;text-align:center;top:1043px}
.person h4{font-family:"Montserrat",sans-serif;font-weight:700;font-size:7.5px;color:var(--ink);margin-bottom:6px}
.person p{font-size:6.6px;line-height:8.8px}

.footer{top:1131px;left:0;width:732px;height:69px;background:var(--footer)}
.copyright{right:80px;top:1157px;font-size:7.5px;color:#ddd}
</style>
</head>
<body>

<header class="hero" role="img" aria-label="Photo of a crowd of protesters raising fists"></header>
<div class="brand abs" style="left:79px;top:10px"><span class="brand-dot"></span><span class="brand-name">Rise Up</span></div>
<nav class="nav abs"><a href="#">Post Action</a><a href="#">Your action</a><a href="#">Register</a><a class="login" href="#">Login</a></nav>
<h1 class="hero-title abs">RACIAL JUSTICE</h1>
<p class="hero-lead abs">Lorem Ipsum is simply dummy text of the printing and types<br>etting industry lorem Ipsum has been the industry.</p>
<a class="cta abs" href="#">Glide web store</a>

<h2 class="heading section-title abs" style="top:304px">HOW THE GLIDE EXTENSION WORKS</h2>
<div class="rule abs" style="left:351px;top:334px;width:30px"></div>

<svg class="abs" style="left:0;top:279px" width="732" height="323" viewBox="0 279 732 323">
  <defs><filter id="soft" x="-30%" y="-30%" width="160%" height="170%"><feDropShadow dx="0" dy="10" stdDeviation="8" flood-color="#000" flood-opacity=".12"/></filter></defs>
  <g fill="#fff" filter="url(#soft)">
    <circle cx="171" cy="459" r="88"/><circle cx="366" cy="459" r="88"/><circle cx="563" cy="459" r="88"/>
  </g>
  <circle cx="171" cy="459" r="81" fill="none" stroke="var(--orange)" stroke-width="4"/>
  <circle cx="366" cy="459" r="81" fill="none" stroke="var(--orange-mid)" stroke-width="4"/>
  <circle cx="563" cy="459" r="81" fill="none" stroke="var(--orange-soft)" stroke-width="4"/>
  <g fill="none" stroke="var(--orange)" stroke-width="1.8">
    <path d="M96 386 A108 108 0 0 1 240 377"/>
    <path d="M488 386 A108 108 0 0 1 632 377"/>
    <path d="M291 533 A108 108 0 0 0 436 540" stroke="var(--orange-mid)"/>
  </g>
  <g fill="var(--orange)">
    <path d="M245 385 L233 380 L242 372 Z"/>
    <path d="M637 385 L625 380 L634 372 Z"/>
    <path d="M441 534 L438 546 L430 539 Z" fill="var(--orange-mid)"/>
  </g>
  <g stroke="#111" stroke-width="1.5" fill="#fff">
    <line x1="252" y1="457" x2="283" y2="457"/><line x1="449" y1="457" x2="481" y2="457"/>
    <circle cx="252" cy="457" r="5"/><circle cx="283" cy="457" r="5"/>
    <circle cx="449" cy="457" r="5"/><circle cx="481" cy="457" r="5"/>
  </g>
  <g fill="none" stroke="var(--orange)" stroke-width="1.5">
    <circle cx="167" cy="417" r="11"/><circle cx="167" cy="417" r="5"/>
    <path d="M174 429 L189 404 L193 407 L178 432 L173 434 Z"/>
    <path d="M356 402 h16 v26 h-16 Z M360 409 h8 M360 414 h8 M360 419 h8 M372 415 h6 v13 h-6"/>
    <circle cx="563" cy="418" r="15"/>
  </g>
</svg>
<div class="step abs" style="left:106px;top:447px"><h3>LOREM IPSUM</h3><p>There are many variations of passages of Lorem Ipsum available, but the majority have suffered alteration in some form, by injected humour, or randomised</p></div>
<div class="step abs" style="left:301px;top:447px"><h3>LOREM IPSUM</h3><p>There are many variations of passages of Lorem Ipsum available, but the majority have suffered alteration in some form, by injected humour, or randomised</p></div>
<div class="step abs" style="left:498px;top:447px"><h3>LOREM IPSUM</h3><p>There are many variations of passages of Lorem Ipsum available, but the majority have suffered alteration in some form, by injected humour, or randomised</p></div>

<section class="overview abs"></section>
<div class="abs" style="left:84px;top:631px;width:182px;height:182px;border-radius:50%;background:var(--peach)"></div>
<div class="abs" style="left:309px;top:634px;width:1px;height:174px;background:#ccc"></div>
<h2 class="heading abs" style="left:370px;top:632px;font-size:11.5px">OVERVIEW</h2>
<div class="rule abs" style="left:370px;top:654px;width:64px"></div>
<div class="overview-body abs">
  <p>Facilitating social responsibility by connecting like minded individuals and to ways they may impact the real world</p>
  <p>Many of us read about social and political issues we care about every day, but may not know how to take concrete action to combat injustice and create meaningful change. Rise Up is a Glide extension that analyzes articles you are reading and recommends relevant actions you can take. By connecting you to organizers and movements, Rise Up can help you find ways to take part in building a more just, equitable, and sustainable future.</p>
</div>

<h2 class="heading section-title abs" style="top:868px">ORGANIZERS</h2>
<div class="rule abs" style="left:326px;top:890px;width:80px"></div>

<svg class="abs" style="left:0;top:910px" width="732" height="130" viewBox="0 910 732 130">
  <g fill="none" stroke="var(--orange)" stroke-width="0.8">
    <path d="M81 975 H106 A53 53 0 0 1 212 975 H241"/>
    <path d="M216 984 H243 A53 53 0 0 0 349 984 H377"/>
    <path d="M352 975 H379 A53 53 0 0 1 485 975 H513"/>
    <path d="M488 984 H515 A53 53 0 0 0 621 984 H648"/>
  </g>
  <g fill="var(--orange)">
    <circle cx="81" cy="975" r="2.6"/><circle cx="241" cy="975" r="2.6"/>
    <circle cx="216" cy="984" r="2.6"/><circle cx="377" cy="984" r="2.6"/>
    <circle cx="352" cy="975" r="2.6"/><circle cx="513" cy="975" r="2.6"/>
    <circle cx="488" cy="984" r="2.6"/><circle cx="648" cy="984" r="2.6"/>
    <circle cx="159" cy="975" r="48"/><circle cx="296" cy="984" r="48"/>
    <circle cx="432" cy="975" r="48"/><circle cx="568" cy="984" r="48"/>
  </g>
  <circle cx="159" cy="975" r="39" fill="#b9b6b4" role="img" aria-label="Portrait photo of Mark"/>
  <circle cx="296" cy="984" r="39" fill="#b3aea9" role="img" aria-label="Portrait photo of Smith"/>
  <circle cx="432" cy="975" r="39" fill="#b8cadb" role="img" aria-label="Portrait photo of Richard"/>
  <circle cx="568" cy="984" r="39" fill="#c3d3e2" role="img" aria-label="Portrait photo of Stanly"/>
</svg>
<div class="person abs" style="left:99px"><h4>MARK</h4><p>There are many variations of passages of Lorem Ipsum available, but the majority have suffered alteration in some form, by injected.</p></div>
<div class="person abs" style="left:241px"><h4>SMITH</h4><p>There are many variations of passages of Lorem Ipsum available, but the majority have suffered alteration in some form, by injected.</p></div>
<div class="person abs" style="left:374px"><h4>RICHARD</h4><p>There are many variations of passages of Lorem Ipsum available, but the majority have suffered alteration in some form, by injected.</p></div>
<div class="person abs" style="left:518px"><h4>STANLY</h4><p>There are many variations of passages of Lorem Ipsum available, but the majority have suffered alteration in some form, by injected.</p></div>

<footer class="footer abs"></footer>
<div class="brand abs" style="left:81px;top:1141px"><span class="brand-dot"></span><span class="brand-name">Rise Up</span></div>
<p class="copyright abs">Copyright © 2022 All Rights Reserved</p>

</body>
</html>
```